Transform this table

Please make a 2 page A4 handout from this boring table into an engaging design. The front page can be simple and engaging (a summary of the back where all the detail lives)

Target Market(s)

Business

Requirements
Must have
• Clarity. And impact.
Nice to have
• Icons

```html
<!DOCTYPE html>
<html lang="en">
<head>
<meta charset="utf-8">
<title>Safety Culture Maturity Ladder – Handout</title>
<link href="https://fonts.googleapis.com/css2?family=Bebas+Neue&family=Lato:ital,wght@0,400;0,700;0,900;1,400;1,700&display=swap" rel="stylesheet">
<style>
:root{
  --backdrop:#9b9b9b;
  --paper:#ffffff;
  --maroon:#7d0a0c;
  --band:#8e1116;
  --red:#d9242b;
  --coral:#f26b3a;
  --orange:#f7941d;
  --lime:#8fbc25;
  --teal:#16a184;
  --ink:#1a1a1a;
  --grey-band:#eeeeee;
  --col-grey:#efefef;
}
*{margin:0;padding:0;box-sizing:border-box}
html,body{width:1200px;height:1200px;overflow:hidden}
body{background:var(--backdrop);position:relative;font-family:"Lato",Arial,sans-serif;color:var(--ink)}
.page{position:absolute;top:206px;width:527px;height:745px;background:var(--paper);overflow:hidden}
.page--front{left:54px}
.page--back{left:621px}
.page-header{position:absolute;left:0;top:0;width:100%;background:var(--maroon);color:#fff;font-family:"Bebas Neue",Impact,sans-serif;text-align:center;letter-spacing:.5px}
.page--front .page-header{height:70px;font-size:40px;line-height:74px}
.page--back .page-header{height:49px;font-size:34px;line-height:52px}
.abs{position:absolute}
.ladder-svg{position:absolute;left:0;top:0}
.step-name{position:absolute;font-family:"Bebas Neue",Impact,sans-serif;font-size:21px;line-height:1}
.step-goal{position:absolute;font-size:9.5px;line-height:12px;text-align:right}
.card-text{position:absolute;color:#fff;text-align:center;font-size:7.5px;line-height:10px;text-transform:uppercase;letter-spacing:.2px}
.card-quote{position:absolute;color:#fff;text-align:center;font-size:9px;line-height:11px}
.icon-slot{position:absolute;border-radius:50%;background:rgba(255,255,255,.28)}
.trend-label{position:absolute;left:118px;top:562px;font-size:19px;line-height:23px;color:#8a8a8a;font-style:italic;transform:rotate(-23deg);transform-origin:left top;white-space:nowrap;letter-spacing:.2px}
.front-footer{position:absolute;left:0;top:651px;width:100%;height:66px;background:var(--grey-band)}
.front-footer h2{position:absolute;left:0;top:9px;width:100%;text-align:center;font-weight:400;font-size:25px;line-height:28px}
.front-footer .rule{position:absolute;top:24px;height:3px;background:var(--maroon);width:95px}
.front-footer p{position:absolute;left:0;top:44px;width:100%;text-align:center;font-size:11px}
.front-strip{position:absolute;left:0;top:717px;width:100%;height:28px;background:var(--maroon);color:#fff;text-align:center;font-size:11px;line-height:28px;font-style:italic;font-weight:700}
.col-bg{position:absolute;top:124px;width:91px;height:605px;background:var(--col-grey)}
.col-head{position:absolute;top:59px;width:91px;height:63px;color:#fff;font-family:"Bebas Neue",Impact,sans-serif;font-size:21px;text-align:center;line-height:66px}
.bullets{position:absolute;list-style:none;font-size:6.6px;line-height:8px;width:84px}
.bullets li{padding-left:5px;position:relative}
.bullets li::before{content:"";position:absolute;left:0;top:3px;width:2.5px;height:2.5px;border-radius:50%;background:var(--red)}
.stage-name{position:absolute;width:91px;text-align:center;font-size:12.5px;line-height:13px;font-weight:700;text-transform:uppercase}
.card-big{position:absolute;color:#fff;text-align:center;font-size:12px;line-height:13px;font-weight:700;text-transform:uppercase}
</style>
</head>
<body>

<section class="page page--front">
  <header class="page-header">Safety Culture Maturity Ladder</header>

  <svg class="ladder-svg" width="527" height="745" viewBox="0 0 527 745" aria-hidden="true">
    <defs>
      <linearGradient id="trend" x1="0" y1="1" x2="1" y2="0">
        <stop offset="0" stop-color="#d9242b"/>
        <stop offset=".5" stop-color="#f7941d"/>
        <stop offset="1" stop-color="#8fbc25"/>
      </linearGradient>
    </defs>
    <polygon points="70,394 118,394 118,334 210,334 210,310 305,310 305,270 400,270 400,240 460,240 460,340 400,340 400,380 305,380 305,420 210,420 210,460 118,460 118,490 70,490" fill="var(--band)"/>
    <path d="M26,394 h86 v107 a43,43 0 0 1 -86,0 z" fill="var(--red)"/>
    <path d="M118,324 h88 v114 a44,44 0 0 1 -88,0 z" fill="var(--coral)"/>
    <path d="M214,299 h87 v101 a43,43 0 0 1 -87,0 z" fill="var(--orange)"/>
    <path d="M308,256 h86 v103 a43,43 0 0 1 -86,0 z" fill="var(--lime)"/>
    <path d="M404,224 h-20 l62,-30 l62,30 h-20 v100 a42,42 0 0 1 -84,0 z" fill="var(--teal)"/>
    <g fill="none" stroke="var(--coral)" stroke-width="3"><path d="M92,330 v-14 h22"/><path d="M110,310 l6,6 l-6,6"/></g>
    <g fill="none" stroke="var(--orange)" stroke-width="3"><path d="M186,292 v-16 h22"/><path d="M204,270 l6,6 l-6,6"/></g>
    <g fill="none" stroke="var(--lime)" stroke-width="3"><path d="M284,256 v-16 h22"/><path d="M302,234 l6,6 l-6,6"/></g>
    <g fill="none" stroke="var(--teal)" stroke-width="3"><path d="M376,204 v-16 h22"/><path d="M394,182 l6,6 l-6,6"/></g>
    <path d="M72,567 L466,405" stroke="url(#trend)" stroke-width="9" stroke-linecap="round"/>
    <path d="M446,394 L472,403 L460,428" fill="none" stroke="#8fbc25" stroke-width="8" stroke-linecap="round" stroke-linejoin="round"/>
  </svg>

  <p class="step-goal" style="left:277px;top:147px;width:128px;color:var(--teal)">Develop consistency<br>&amp; fight complacency</p>
  <p class="step-goal" style="left:149px;top:196px;width:160px;color:var(--lime)">All team members engaged<br>&amp; all risks &nbsp;controlled</p>
  <p class="step-goal" style="left:90px;top:235px;width:117px;color:var(--orange)">Standardise processes<br>&amp; gain commitment</p>
  <p class="step-goal" style="left:30px;top:270px;width:100px;color:var(--coral);text-align:left">Wake management<br>&amp; control high risks</p>

  <span class="step-name" style="left:30px;top:356px;color:var(--red)">Vulnerable</span>
  <span class="step-name" style="left:131px;top:299px;color:var(--coral)">Reactive</span>
  <span class="step-name" style="left:224px;top:265px;color:var(--orange)">Compliant</span>
  <span class="step-name" style="left:321px;top:229px;color:var(--lime)">Proactive</span>
  <span class="step-name" style="left:413px;top:177px;color:var(--teal)">Resilient</span>

  <div class="icon-slot" role="img" aria-label="Icon: head with a prohibition sign" style="left:54px;top:396px;width:32px;height:32px"></div>
  <div class="icon-slot" role="img" aria-label="Icon: pointing hand" style="left:146px;top:348px;width:32px;height:32px"></div>
  <div class="icon-slot" role="img" aria-label="Icon: checklist clipboard" style="left:242px;top:310px;width:32px;height:32px"></div>
  <div class="icon-slot" role="img" aria-label="Icon: lightbulb linked to a team" style="left:335px;top:268px;width:32px;height:32px"></div>
  <div class="icon-slot" role="img" aria-label="Icon: figure climbing steps to a flag" style="left:430px;top:218px;width:32px;height:32px"></div>

  <p class="card-text" style="left:26px;top:443px;width:86px">Toxic / No care<br>culture</p>
  <p class="card-quote" style="left:26px;top:478px;width:86px">“Accidents<br>happen”</p>
  <p class="card-text" style="left:118px;top:393px;width:88px">Blame culture</p>
  <p class="card-quote" style="left:118px;top:416px;width:88px">“It was<br>an accident!”</p>
  <p class="card-text" style="left:214px;top:366px;width:87px">Compliance<br>culture</p>
  <p class="card-quote" style="left:214px;top:401px;width:87px">“Incidents<br>have causes”</p>
  <p class="card-text" style="left:308px;top:326px;width:86px">Ownership<br>culture</p>
  <p class="card-quote" style="left:308px;top:358px;width:86px">“We prevent<br>incidents”</p>
  <p class="card-text" style="left:404px;top:278px;width:84px">Interdependent<br>culture</p>
  <p class="card-quote" style="left:404px;top:312px;width:84px">“It’s how<br>we do business.”</p>

  <span class="trend-label">Increasing Accountability &amp; Reliability</span>

  <footer class="front-footer">
    <span class="rule" style="left:12px"></span>
    <h2>Improving Safety Culture</h2>
    <span class="rule" style="right:12px"></span>
    <p>Based on the Harlow Institute and Daniel Marsh “hearts and minds” model</p>
  </footer>
  <div class="front-strip">Develop your cultural maturity - www.stepwisesafety.com</div>
</section>

<section class="page page--back">
  <header class="page-header">Safety Culture Maturity Ladder</header>

  <div class="col-bg" style="left:12px"></div>
  <div class="col-bg" style="left:111px"></div>
  <div class="col-bg" style="left:212px"></div>
  <div class="col-bg" style="left:311px"></div>
  <div class="col-bg" style="left:410px"></div>

  <div class="col-head" style="left:12px;background:var(--red)">Vulnerable</div>
  <div class="col-head" style="left:111px;background:var(--coral)">Reactive</div>
  <div class="col-head" style="left:212px;background:var(--orange)">Compliant</div>
  <div class="col-head" style="left:311px;background:var(--lime)">Proactive</div>
  <div class="col-head" style="left:410px;background:var(--teal)">Resilient</div>

  <ul class="bullets" style="left:15px;top:131px">
    <li>Apathy / resistance</li><li>Near misses not considered</li><li>Negligence</li><li>Dishonesty</li><li>Hiding of incidents</li><li>Serious injury / health risks are unseen or ignored</li><li>Unfair disciplinary actions</li><li>No or little training</li><li>Poor or no communication</li><li>Production at almost any cost</li><li>“Just get it done” attitude or blatantly unsafe</li>
  </ul>
  <ul class="bullets" style="left:114px;top:131px">
    <li>Dependent on natural instincts</li><li>Accept need to care</li><li>Some near miss reporting</li><li>Some window dressing e.g. pre-inspection cleanups and light duty</li><li>Disciplinary action</li><li>Minimum / inconsistent training</li><li>Some communication on a need to know basis</li>
  </ul>
  <ul class="bullets" style="left:215px;top:131px">
    <li>Supervision dependent</li><li>Some participation</li><li>Near miss discussions</li><li>Acceptable training / awareness</li><li>Established and good communication channels</li><li>Regular people involvement and focus</li>
  </ul>
  <ul class="bullets" style="left:314px;top:131px">
    <li>Involvement at all levels</li><li>Near miss involvement</li><li>High level of training / awareness</li><li>Communication at a high level hiding nothing</li>
  </ul>
  <ul class="bullets" style="left:413px;top:131px">
    <li>Way of life</li><li>Comes natural</li><li>Personal involvement by all to manage risks well &amp; prevent incidents</li><li>Authentic communication throughout culture</li>
  </ul>

  <svg class="ladder-svg" width="527" height="745" viewBox="0 0 527 745" aria-hidden="true">
    <polygon points="60,395 111,395 111,330 212,330 212,300 311,300 311,260 410,260 410,250 470,250 470,350 410,350 410,395 311,395 311,440 212,440 212,480 111,480 111,500 60,500" fill="var(--band)"/>
    <path d="M12,382 h91 v109 a45.5,45.5 0 0 1 -91,0 z" fill="var(--red)"/>
    <path d="M111,320 h91 v119 a45.5,45.5 0 0 1 -91,0 z" fill="var(--coral)"/>
    <path d="M212,292 h91 v111 a45.5,45.5 0 0 1 -91,0 z" fill="var(--orange)"/>
    <path d="M311,250 h91 v105 a45.5,45.5 0 0 1 -91,0 z" fill="var(--lime)"/>
    <path d="M410,240 h-18 l62,-34 l64,34 h-17 v80 a45.5,45.5 0 0 1 -91,0 z" fill="var(--teal)"/>
  </svg>

  <div class="icon-slot" role="img" aria-label="Icon: head with a prohibition sign" style="left:34px;top:392px;width:46px;height:46px"></div>
  <div class="icon-slot" role="img" aria-label="Icon: pointing hand" style="left:133px;top:340px;width:46px;height:46px"></div>
  <div class="icon-slot" role="img" aria-label="Icon: checklist clipboard" style="left:234px;top:302px;width:46px;height:46px"></div>
  <div class="icon-slot" role="img" aria-label="Icon: lightbulb linked to a team" style="left:333px;top:260px;width:46px;height:46px"></div>
  <div class="icon-slot" role="img" aria-label="Icon: figure climbing steps to a flag" style="left:432px;top:236px;width:46px;height:46px"></div>

  <p class="card-big" style="left:12px;top:467px;width:91px">Accept<br>that<br>accidents<br>happen</p>
  <p class="card-big" style="left:111px;top:409px;width:91px">Prevent<br>a similar<br>accident</p>
  <p class="card-big" style="left:212px;top:367px;width:91px">Write and<br>enforce<br>procedures</p>
  <p class="card-big" style="left:311px;top:339px;width:91px">Manage<br>risks<br>well</p>
  <p class="card-big" style="left:410px;top:310px;width:91px">Way we do<br>business</p>

  <p class="stage-name" style="left:12px;top:546px;color:var(--red)">Toxic<br>/ No care<br>culture</p>
  <p class="stage-name" style="left:111px;top:495px;color:var(--coral)">Blame<br>culture</p>
  <p class="stage-name" style="left:212px;top:463px;color:var(--orange)">Compliance<br>culture</p>
  <p class="stage-name" style="left:311px;top:411px;color:var(--lime)">Independent<br>&amp; personal<br>ownership<br>culture</p>
  <p class="stage-name" style="left:410px;top:378px;color:var(--teal);font-size:9.5px;line-height:12px">Interdependent<br><span style="font-size:12.5px;line-height:13px">team<br>culture</span></p>

  <ul class="bullets" style="left:15px;top:597px">
    <li>Reactive or unresponsive approach</li><li>No OHS systems</li><li>No risk assessment</li><li>Legal non compliance</li><li>Accept equipment / process decay</li><li>Only fix when broken / unsafe repairs</li><li>Reports are shelved / used irresponsibly</li><li>No or poor investigation</li><li>No monitoring / audits</li><li>Permit non-compliance</li><li>Potential illegal practices</li>
  </ul>
  <ul class="bullets" style="left:114px;top:533px">
    <li>Administrator driven</li><li>Loose systems, elements of an OHS Management System</li><li>Reactive risk assessment and control</li><li>Minimum legal compliance</li><li>Apply PPE as a way of eliminating exposure</li><li>Incident investigation but limited analysis</li><li>Focus on what happened</li><li>No systems focus</li><li>Human faults occur</li><li>Ad hoc monitoring / audits</li><li>No occupational hygiene or health initiatives</li><li>Reactive medical monitoring</li><li>Monitoring as per regulations</li>
  </ul>
  <ul class="bullets" style="left:215px;top:502px">
    <li>OHS coordinator driven</li><li>OHS standards system and ISO 9002 or equivalent</li><li>Risk assessment through existing systems</li><li>Total legal compliance goal</li><li>Strictly enforced the use of PPE where required (knowing risk)</li><li>Causal incident analysis based on events potential</li><li>Info sharing from events</li><li>Planned occupational hygiene / environmental monitoring</li><li>Periodical medical examinations</li><li>Planned monitoring / audits</li><li>Safety meetings &amp; talks</li><li>Some task observations</li>
  </ul>
  <ul class="bullets" style="left:314px;top:474px">
    <li>Committed leadership at all levels</li><li>Line driven systems improvement</li><li>ISO 14001 &amp; ISO 45001</li><li>Pro-active formal risk management</li><li>Beyond legal compliance</li><li>Seek to actively engineer out process / equipment inadequacies</li><li>Incident learnings shared with all levels</li><li>Well designed plans / procedures</li><li>Focus on adhering to site plans &amp; procedures</li><li>Integrated audits</li><li>Peer evaluations and discussion</li>
  </ul>
  <ul class="bullets" style="left:413px;top:428px">
    <li>Individually internalized</li><li>Inspiring genuine leadership</li><li>No silo thinking or actions</li><li>All staff active, positive, respected, speaking up</li><li>Excellent equipment, ultra-organised</li><li>Integrated management systems</li><li>Risk management cycle integrated into all systems</li><li>Self regulating style</li><li>Eliminate &amp; prevent problems before they occur</li><li>All threats considered in decision-making</li><li>Continually improving through external evaluation / auditing</li><li>Multiple positive performance indicators drive PDCA cycle</li>
  </ul>

  <div class="abs" style="left:0;bottom:0;width:100%;height:8px;background:var(--maroon)"></div>
</section>

</body>
</html>
```